Geschäftspapiere für Coaching und Talent Management
Professionell und freundlich
Zielgruppe
Zielgruppe: Führungskräfte
Tätigkeit: Führungskräfte Coaching und Talent Management
Aufgabenstellung
- Der Briefbogen soll klar und smart/elegant wirken
- Das Logo wurde gerade neu erstellt und füge ich bei
- Die weiteren Daten lade ich hoch sobald der Gewinner gewählt ist. Bitte beim Design beachten, dass folg Informationen zusätzlich zum Logo auf das Briefpapier sollen:
Postleitzahl und Stadt
Strasse und Hausnummer
Website und Email Kontakt
Umsatz St.Nr

```html
<!DOCTYPE html>
<html lang="de">
<head>
<meta charset="utf-8">
<title>Marlene Vossberg – Briefbogen</title>
<link href="https://fonts.googleapis.com/css2?family=Lato:wght@400;700&display=swap" rel="stylesheet">
<style>
  :root {
    --backdrop: #9c9c9c;
    --paper: #ffffff;
    --ink-dark: #2a4650;
    --accent: #d24b2a;
    --fold-mark: #e39a86;
    --watermark: #f3f3f3;
  }
  html, body {
    margin: 0;
    padding: 0;
    width: 1200px;
    height: 1200px;
    overflow: hidden;
    background: var(--backdrop);
  }
  .letterhead {
    position: absolute;
    left: 212px;
    top: 52px;
    width: 775px;
    height: 1096px;
    background: var(--paper);
    font-family: "Lato", sans-serif;
    overflow: hidden;
  }
  .band {
    position: absolute;
    left: 19px;
    width: 738px;
    height: 9px;
  }
  .band--top { top: 11px; background: var(--ink-dark); }
  .band--bottom { top: 1078px; background: var(--accent); }

  .brand__dot {
    position: absolute;
    left: 255px;
    top: 67px;
    width: 30px;
    height: 30px;
    border-radius: 50%;
    background: var(--accent);
  }
  .brand__divider {
    position: absolute;
    left: 306px;
    top: 55px;
    width: 1px;
    height: 49px;
    background: var(--ink-dark);
  }
  .brand__name {
    position: absolute;
    left: 315px;
    top: 63px;
    font-size: 21px;
    font-weight: 400;
    letter-spacing: 0.9px;
    color: var(--accent);
    line-height: 1;
    white-space: nowrap;
  }
  .brand__tagline {
    position: absolute;
    left: 316px;
    top: 86px;
    font-size: 8px;
    font-weight: 700;
    letter-spacing: 6.3px;
    color: var(--ink-dark);
    line-height: 1;
    white-space: nowrap;
  }

  .fold-mark {
    position: absolute;
    left: 0;
    width: 37px;
    height: 1px;
    background: var(--fold-mark);
  }
  .fold-mark--upper { top: 388px; }
  .fold-mark--middle { top: 548px; }
  .fold-mark--lower { top: 775px; }

  .watermark {
    position: absolute;
    left: 0;
    top: 0;
  }
</style>
</head>
<body>
  <main class="letterhead">
    <div class="band band--top"></div>

    <header class="brand">
      <span class="brand__dot"></span>
      <span class="brand__divider"></span>
      <span class="brand__name">MARLENE VOSSBERG</span>
      <span class="brand__tagline">THE LEADERSHIP COACH</span>
    </header>

    <div class="fold-mark fold-mark--upper"></div>
    <div class="fold-mark fold-mark--middle"></div>
    <div class="fold-mark fold-mark--lower"></div>

    <svg class="watermark" width="775" height="1096" viewBox="0 0 775 1096" aria-hidden="true">
      <circle cx="387" cy="872" r="165" fill="none" stroke="var(--watermark)" stroke-width="36"/>
    </svg>

    <div class="band band--bottom"></div>
  </main>
</body>
</html>
```